Corvain Skydrift Gala web site design

"Corvain" Yearly Lofting Skydrift Gala. Be sure to spell Balloon proprely! The largest in the state of Texas. In a park setting with sky divers, live concerts, 5K run event, kids fun zones, food vendors, merchandise, fireowrks, arts & crafts, family oriented, very colorful. Would like to establish themselves as the only event of it's kind in the region. Would like to convey that the event is very cost friendly and a unique experience relative to the other family entertainment opportunities in the area. Easy to read! Would like to emulate various features of www.driftgalaxo.com

Target Market(s)

Families. Kids up to 12. Then adults 25 to 80.

Industry/Entity Type

Entertainment

Requirements
Must have
• Ease of use for participants. There will be an area dedicated to each of the following categories: Attendees, Pilots, Vendors, Volunteers, Performers. Directions, event schedule and tickets will be critical call outs. Then details and sign up info for the other 4 categories. Will need a register/login feature.
Nice to have
• Weather conditions feature, countdown to event clock, social media integration to home page, youtube channel with videos of launch, custom static background image to frame header and content area.
Should not have
• Dark dreary colors or hard to read fonts.

```html
<!DOCTYPE html>
<html lang="en">
<head>
<meta charset="utf-8">
<title>Corvain Skydrift Gala</title>
<link rel="stylesheet" href="https://fonts.googleapis.com/css2?family=Arimo:wght@400;700&family=Tinos:ital@1&family=Roboto+Condensed:wght@400;700&display=swap">
<style>
:root{
  --bg-top:#0a4a86;
  --bg-bottom:#00acf2;
  --nav-top:#5cc6f8;
  --nav-bottom:#1a9fe6;
  --side:#6b9ad2;
  --side-line:#86addc;
  --side-band:#0b73bd;
  --gold:#f3e04a;
  --panel:#d5e7f8;
  --panel-line:#b9d3ec;
  --ink:#0d3f73;
  --pink:#e8457b;
  --orange:#f4b400;
  --sky:#3f95d6;
  --green:#7cc244;
  --card-foot:#2a88cf;
  --white:#ffffff;
  --social:#f08a00;
}
*{margin:0;padding:0;box-sizing:border-box}
html,body{width:1200px;height:900px;overflow:hidden}
body{background:linear-gradient(var(--bg-top),var(--bg-bottom) 70%);font-family:Arimo,Arial,sans-serif;position:relative;color:var(--ink)}
.abs{position:absolute}
.event-date{left:200px;top:62px;font:italic 30px Tinos,serif;color:var(--white)}
.date-balloon{left:118px;top:60px;width:60px;height:76px}
.countdown{left:884px;top:65px;display:flex;gap:12px;align-items:center}
.countdown .unit{font:700 12px/13px Arimo,sans-serif;color:var(--gold)}
.countdown .unit b{display:block;color:var(--white)}
.header-sky{left:113px;top:100px;width:976px;height:221px;background:linear-gradient(#3aa2e8,#bfe3fa 60%,#e6f4fd)}
.logo{left:138px;top:140px;font:700 62px/1 Arimo,sans-serif;color:var(--pink);letter-spacing:1px}
.logo-sub{left:140px;top:208px;font:700 22px Roboto Condensed,sans-serif;color:#1577c9}
.header-photo{left:505px;top:58px;width:584px;height:263px}
.tagline{left:660px;top:240px;font:700 27px Arimo,sans-serif;color:var(--white);transform:rotate(-22deg);transform-origin:left top;letter-spacing:1px}
.main-nav{left:106px;top:321px;width:991px;height:39px;background:linear-gradient(var(--nav-top),var(--nav-bottom));display:flex;align-items:center;justify-content:space-between;padding:0 27px 0 26px}
.main-nav a{font:700 12px Arimo,sans-serif;color:var(--white);text-decoration:none;white-space:nowrap}
.content{left:113px;top:360px;width:976px;height:437px;background:var(--white)}
.sidebar{left:113px;top:360px;width:212px;height:437px;background:var(--side);color:var(--white)}
.side-title{font:700 14px Arimo,sans-serif;color:var(--gold);position:absolute;left:16px}
.field-label{position:absolute;left:16px;font-size:12px}
.field{position:absolute;left:16px;width:179px;height:22px;background:var(--white)}
.btn{position:absolute;height:26px;border-radius:6px;background:linear-gradient(#fff,#e3edf6);border:1px solid #b4c8dc;font:12px Arimo,sans-serif;color:#17406d;display:flex;align-items:center;justify-content:center}
.forgot{left:92px;top:139px;font:700 11px Arimo,sans-serif;color:#e2ecf7}
.new-user{position:absolute;left:0;top:170px;width:212px;height:50px;background:var(--side-band);padding:7px 18px;font-size:11px}
.new-user b{display:block}
.new-user u{font-size:12px}
.quick-links{position:absolute;left:0;top:254px;width:212px;list-style:none}
.quick-links li{height:30px;border-bottom:1px solid var(--side-line);padding:9px 0 0 18px;font-size:12px}
.card{position:absolute;top:371px;width:177px;height:246px;border-radius:10px;overflow:hidden;background:var(--card-foot)}
.card h3{height:24px;font:700 13px/24px Arimo,sans-serif;color:var(--white);text-align:center}
.card .photo{height:142px}
.card p{padding:12px 4px 0 17px;font:700 11.5px/18px Arimo,sans-serif;letter-spacing:-.2px;color:var(--white)}
.info-panel{left:337px;top:629px;width:741px;height:161px;background:var(--panel);display:flex}
.info-panel>section{position:relative;border-right:1px solid var(--panel-line)}
.panel-title{position:absolute;left:11px;top:12px;font:16px Arimo,sans-serif;color:var(--pink)}
.weather dl{position:absolute;left:11px;top:53px;font-size:10px;display:grid;grid-template-columns:78px auto;row-gap:6px}
.weather dt{font-weight:700}
.more{position:absolute;left:11px;top:125px;font-size:10.5px;text-decoration:underline}
.newsletter .label{position:absolute;left:10px;top:52px;font:700 11px Arimo,sans-serif}
.call-list{padding:4px 8px 0 8px;width:244px}
.call{display:flex;align-items:center;gap:10px;height:40px;border-bottom:1px solid var(--white);font:22px Roboto Condensed,sans-serif;color:#17467c;padding-left:2px}
.social{display:flex;gap:22px;padding:6px 0 0 6px}
.social span{display:flex;gap:6px;font:700 11px/13px Arimo,sans-serif;color:var(--social)}
.social i{width:24px;height:24px;background:#3c6fb4;display:block}
.social span+span i{background:#7cc8ee}
.footer{left:113px;top:805px;font-size:11.5px;color:var(--white)}
</style>
</head>
<body>
<svg class="abs date-balloon" role="img" aria-label="Striped hot air balloon illustration"><ellipse cx="30" cy="30" rx="29" ry="29" fill="#e5562f"/><rect x="23" y="62" width="14" height="10" fill="#8a5a2a"/></svg>
<div class="abs event-date">24th April 2011</div>
<div class="abs countdown">
  <svg width="28" height="28" viewBox="0 0 28 28"><circle cx="14" cy="14" r="12" fill="none" stroke="#fff" stroke-width="2.5"/><path d="M14 7v7l5 3" stroke="#fff" stroke-width="2" fill="none"/></svg>
  <div class="unit">DAYS<b>65</b></div><div class="unit">HOUR<b>18</b></div><div class="unit">MIN<b>30</b></div><div class="unit">SEC<b>11</b></div>
</div>

<div class="abs header-sky" role="img" aria-label="Bright sky with clouds and floating hot air balloons"></div>
<div class="abs logo">CORVAIN</div>
<div class="abs logo-sub">Yearly Lofting Skydrift Gala</div>
<svg class="abs header-photo" viewBox="0 0 584 263" role="img" aria-label="Photo of colorful hot air balloons inflating with fireworks">
  <defs><linearGradient id="hp" x1="0" y1="0" x2="1" y2="1"><stop offset="0" stop-color="#f0c232"/><stop offset=".45" stop-color="#d6344a"/><stop offset=".75" stop-color="#2c5fb5"/><stop offset="1" stop-color="#46c8e8"/></linearGradient></defs>
  <path d="M0 263 C40 120 100 20 220 8 C330 -2 360 40 440 60 C500 75 540 55 584 40 V263 Z" fill="url(#hp)"/>
  <path d="M130 215 C250 205 340 170 400 205 C450 235 500 245 584 200 V263 H150 Z" fill="#fff" opacity=".9"/>
</svg>
<div class="abs tagline">A UNIQUE EXPERIENCE</div>

<nav class="abs main-nav">
  <a>EVENT INFO ▼</a><a>GUEST GUIDE ▼</a><a>GAS BALLOONS ▼</a><a>PILOTS AND CREW ▼</a><a>BALLOONING ▼</a><a>OPERATIONS ▼</a><a>SPONSORS ▼</a><a>MERCHANDISE</a><a>MEDIA</a>
</nav>

<div class="abs content"></div>
<aside class="abs sidebar">
  <div class="side-title" style="top:11px">LOGIN</div>
  <div class="field-label" style="top:36px">User Name</div>
  <div class="field" style="top:54px"></div>
  <div class="field-label" style="top:84px">Password</div>
  <div class="field" style="top:100px"></div>
  <div class="btn" style="left:16px;top:133px;width:72px">LOGIN ››</div>
  <div class="abs forgot">Forgot Password?</div>
  <div class="new-user"><b>New User?</b><u>Click Here to Register</u></div>
  <div class="side-title" style="top:231px">Quick Link</div>
  <ul class="quick-links">
    <li>›› Attendees</li><li>›› Pilots</li><li>›› Vendors</li><li>›› Volunteers</li><li>›› Performers</li>
  </ul>
</aside>

<article class="card" style="left:337px"><h3 style="background:var(--pink)">GUEST GUIDE</h3><div class="photo" role="img" aria-label="Close-up of a pink and yellow balloon envelope" style="background:linear-gradient(135deg,#d8336f,#e9c43a 60%,#c0285a)"></div><p>Everything you'll need to enjoy the Skydrift Gala, Click Here!</p></article>
<article class="card" style="left:524px"><h3 style="background:var(--orange)">BUY A BRICK</h3><div class="photo" role="img" aria-label="Colorful balloons rising over the park" style="background:linear-gradient(#a9cfee,#e55a3c 50%,#f2c43b)"></div><p>Make a lasting memory at Skydrift Gala Park with your own brick!</p></article>
<article class="card" style="left:713px"><h3 style="background:var(--sky)">MERCHANDISE</h3><div class="photo" role="img" aria-label="Skydiver descending with a large flag" style="background:linear-gradient(#cfe1f1,#eef4f9 55%,#9fbf8a)"></div><p>Click here for official Skydrift Gala gear at skydriftgear.com!</p></article>
<article class="card" style="left:901px"><h3 style="background:var(--green)">RV INFORMATION</h3><div class="photo" role="img" aria-label="Food vendors cooking at an outdoor grill" style="background:linear-gradient(135deg,#7d7a70,#c9c3b4 50%,#9a8a6c)"></div><p>Accepting RV reservations for the 2011 Skydrift Gala!</p></article>

<div class="abs info-panel">
  <section class="weather" style="width:238px">
    <div class="panel-title">WEATHER</div>
    <svg class="abs" style="left:130px;top:6px" width="46" height="40"><circle cx="22" cy="16" r="12" fill="#f6c21c"/><ellipse cx="26" cy="28" rx="16" ry="9" fill="#fff"/></svg>
    <dl><dt>Updated</dt><dd>02/17/11 3:36a</dd><dt>Temperature:</dt><dd>49.0F</dd><dt>Wind:</dt><dd>2.0 mph From S (176 Deg.)</dd></dl>
    <div class="more">Click here for more detailed info</div>
  </section>
  <section class="newsletter" style="width:259px">
    <div class="panel-title">FREE NEWSLETTER</div>
    <svg class="abs" style="left:180px;top:8px" width="42" height="28"><rect x="1" y="1" width="40" height="26" fill="#fff" stroke="#aab"/><path d="M1 1l20 14 20-14" fill="none" stroke="#aab"/></svg>
    <div class="label">Enter your email id:</div>
    <div class="field" style="left:10px;top:70px;width:163px;height:24px"></div>
    <div class="btn" style="left:10px;top:103px;width:112px">SUBSCRIBE ››</div>
  </section>
  <section class="call-list">
    <div class="call"><svg width="30" height="30"><rect x="4" y="9" width="24" height="14" rx="2" fill="#e4e6ea" stroke="#999" transform="rotate(-35 16 16)"/></svg>Ticket</div>
    <div class="call"><svg width="30" height="30"><rect x="3" y="5" width="24" height="22" fill="#f4f4f4" stroke="#777"/><rect x="3" y="5" width="24" height="6" fill="#999"/><text x="9" y="24" font-size="11" font-family="Arimo">12</text></svg>Event Schedule</div>
    <div class="call"><svg width="30" height="30"><circle cx="12" cy="15" r="10" fill="#8c8f94"/><circle cx="12" cy="15" r="3" fill="#ddd"/><rect x="18" y="12" width="11" height="8" fill="#666"/></svg>Launch Video</div>
    <div class="social"><span><i></i>Join us on<br>Friendwall</span><span><i></i>Follow us on<br>Chirpline</span></div>
  </section>
</div>

<div class="abs footer">© 2011 corvaingala.com . All rights reserved.</div>
</body>
</html>
```